Corewise Motion Business Cards

Can all designers please apply the following info on their designs' back-side of the business card: (please see brief file upload ('Info for backside...' - for required info, colours & layout)

SPECIALISING IN INDIVIDUAL PILATES INSTRUCTION
MATWORK – including small apparatus
and STUDIO:
VIVANTE 5 REFORMER
LADDER BARREL
MERIDAN BARREL
TENDRA DOME
KALVO CHAIR
TOR-I-VAN

Business Cards for Corewise Motion - applying the Corewise Motion logo design selected earlier.
Note the business card requires both a front and back side. Please refer to two uploaded ppt-files for type of info required to be displayed, and rough position of where info could be. Require innovative / fresh approach to business card design and use of colour by designers now. Please refer to and use logo as uploaded - also for potential business card colour application.

Dear Designers,

Please note the additional inclusion / upload of two draft ppt-files that try to show where I want what type of information, for both the front & back sides of the required business card, plus an attempt at showing the high-level concept / idea of business info position.

As my 'drafts' obviously lack colour and any ability towards innovative card design or approach – I now rely on your vastly superior graphic design abilities to produce a really great business card for my business…

Looking forward to your submissions!

Kind regards, Maren for: Corewise Motion 

Hello all Designers,

Can all designers please apply the following info on their designs' back-side of the business card: (please see / refer to the Brief and specifically the file upload ('Info for backside...' - for required info, colours & layout) - for the backside of the business card).

Info content (without colour, layout etc.):

and STUDIO:

VIVANTE 5 REFORMER

LADDER BARREL

MERIDAN BARREL

TENDRA DOME

KALVO CHAIR

TOR-I-VAN

Thank you to all designers that submitted for consideration!

With regards,

Corewise Motion

```html
<!DOCTYPE html>
<html lang="en">
<head>
<meta charset="utf-8">
<title>Corewise Motion Business Cards</title>
<link rel="stylesheet" href="https://fonts.googleapis.com/css2?family=Open+Sans:ital,wght@0,400;0,600;0,700;1,400&display=swap">
<style>
  :root {
    --backdrop: #dcdcdc;
    --card: #ffffff;
    --brand-orange: #e0531c;
    --band-orange: #ff6a00;
    --brand-green: #4a6e10;
    --band-green: #6aa312;
    --ink: #333333;
    --ink-soft: #444444;
  }
  * { margin: 0; padding: 0; box-sizing: border-box; }
  html, body {
    width: 1200px; height: 1000px; overflow: hidden;
    background: var(--backdrop);
    font-family: "Open Sans", Arial, sans-serif;
  }
  .canvas { position: relative; width: 1200px; height: 1000px; }

  .card {
    position: absolute; top: 325px;
    width: 530px; height: 303px;
    background: var(--card);
  }
  .card--front { left: 58px; }
  .card--back { left: 617px; }

  .band {
    position: absolute; left: 105px;
    width: 320px; height: 23px;
  }
  .band--top { top: 0; }
  .band--bottom { bottom: 0; }
  .card--front .band { background: linear-gradient(to bottom, #4f8a0a, var(--band-green)); }
  .card--front .band--bottom { background: linear-gradient(to top, #78b315, #4f8a0a); }
  .card--back .band { background: linear-gradient(to bottom, #ff5a00, var(--band-orange)); }

  .brand {
    position: absolute; left: 0; right: 0;
    display: flex; align-items: center; justify-content: center; gap: 14px;
  }
  .brand__mark {
    width: 30px; height: 30px; border-radius: 50%;
    background: var(--brand-green); flex: none;
  }
  .brand__name {
    color: var(--brand-orange); font-weight: 400; line-height: 1; white-space: nowrap;
  }
  .card--front .brand { top: 112px; }
  .card--front .brand__name { font-size: 44px; }
  .card--back .brand { top: 36px; }
  .card--back .brand__name { font-size: 36px; }
  .card--back .brand__mark { width: 24px; height: 24px; }

  .tagline {
    position: absolute; top: 175px; left: 0; right: 0;
    text-align: center; color: var(--brand-green);
    font-size: 15px; letter-spacing: 1.5px;
  }
  .tagline__dot { color: var(--brand-orange); margin: 0 8px; }

  .holder { position: absolute; top: 86px; left: 0; right: 0; text-align: center; }
  .holder__name { font-size: 19px; font-weight: 700; color: var(--ink); line-height: 1.2; }
  .holder__title { font-size: 13.5px; font-style: italic; color: var(--ink-soft); margin-top: 2px; line-height: 1.3; }

  .services {
    position: absolute; top: 138px; left: 30px; right: 30px;
    text-align: center; font-size: 9.5px; line-height: 13px;
    letter-spacing: 0.4px; color: var(--ink-soft);
  }
  .services__lead { color: var(--brand-green); font-weight: 600; }
  .services__label { color: var(--brand-orange); font-weight: 600; }

  .contact {
    position: absolute; top: 190px;
    font-size: 15px; line-height: 22px; color: var(--ink);
    white-space: nowrap;
  }
  .contact--studio { left: 40px; }
  .contact--reach { left: 270px; }
  .contact__label { color: var(--brand-orange); }
</style>
</head>
<body>
<main class="canvas">
  <section class="card card--front" aria-label="Card front">
    <div class="band band--top"></div>
    <div class="brand">
      <span class="brand__mark"></span>
      <span class="brand__name">Corewise Motion</span>
    </div>
    <p class="tagline">BALANCE<span class="tagline__dot">•</span>STRENGTH<span class="tagline__dot">•</span>FLEXIBILITY</p>
    <div class="band band--bottom"></div>
  </section>

  <section class="card card--back" aria-label="Card back">
    <div class="band band--top"></div>
    <div class="brand">
      <span class="brand__mark"></span>
      <span class="brand__name">Corewise Motion</span>
    </div>
    <div class="holder">
      <p class="holder__name">Maren Holloway</p>
      <p class="holder__title">Diploma of Professional Pilates Instruction</p>
    </div>
    <div class="services">
      <p class="services__lead">SPECIALISING IN INDIVIDUAL PILATES INSTRUCTION</p>
      <p><span class="services__label">MATWORK</span> – including small apparatus and <span class="services__label">STUDIO:</span></p>
      <p>VIVANTE 5 REFORMER • LADDER BARREL • MERIDAN BARREL • TENDRA DOME • KALVO CHAIR • TOR-I-VAN</p>
    </div>
    <div class="contact contact--studio">
      <p class="contact__label">Studio Location:</p>
      <p>12 Larkspur Avenue</p>
      <p>Westvale WA 6099</p>
    </div>
    <div class="contact contact--reach">
      <p><span class="contact__label">M:</span> 041 555 0192</p>
      <p><span class="contact__label">E:</span>&nbsp; info@corewisemotion.com</p>
      <p><span class="contact__label">W:</span> www.corewisemotion.com.au</p>
    </div>
    <div class="band band--bottom"></div>
  </section>
</main>
</body>
</html>
```